New Business Card Design Project

2 sided business card required. I have attached some previous designs of items we have had made so you can see the logo etc. we Want the card to look professional and modern. for the final design upload for winning designer please note I need to be able to edit the names / phone numbers on the card design as I need to get them made for different staff.
Updates

extending time so designers can have time to submit

Target Market(s)

new customers

Industry/Entity Type

transport / earthmoving

Contact Information for Business Card

name, phone number email address

Requirements
Nice to have
• professional / impressive looking card (first impressions to customers count)
Should not have
• do not put our mobile number on the design use a generic number

```html
<!DOCTYPE html>
<html lang="en">
<head>
<meta charset="utf-8">
<title>KRX Pty Ltd – Business Card</title>
<link rel="stylesheet" href="https://fonts.googleapis.com/css2?family=Nunito+Sans:ital,wght@0,300;0,400;0,600;0,800;1,800&display=swap">
<style>
  :root {
    --page-bg: #e9e9eb;
    --card-black: #0b0b0c;
    --mesh-dark: #1d1d1f;
    --mesh-mid: #3a3a3d;
    --desert-light: #c88a58;
    --desert-deep: #9a5a32;
    --silver: #c9c9cc;
    --text-white: #ffffff;
    --text-soft: #e4e4e6;
    --muted-grey: #8d8d92;
    --service-band: #f3f3f4;
    --bullet-dark: #2d2d30;
    --service-text: #3c3c40;
  }
  * { box-sizing: border-box; margin: 0; padding: 0; }
  html, body {
    width: 1171px; height: 1200px; overflow: hidden;
    background: var(--page-bg);
    font-family: "Nunito Sans", Arial, sans-serif;
  }
  .canvas { position: relative; width: 1171px; height: 1200px; }
  .card {
    position: absolute; left: 201px; width: 768px; height: 441px;
    border-radius: 18px; overflow: hidden; background: var(--card-black);
    box-shadow: 0 6px 20px rgba(0,0,0,.25);
  }
  .card--front { top: 150px; }
  .card--back { top: 650px; }

  /* front */
  .front-photo {
    position: absolute; right: 0; top: 0; width: 66%; height: 100%;
    background:
      linear-gradient(90deg, var(--card-black) 0%, rgba(11,11,12,.55) 30%, rgba(11,11,12,0) 60%),
      linear-gradient(180deg, var(--mesh-dark) 0%, var(--mesh-mid) 40%, #4a4440 58%, var(--desert-light) 78%, var(--desert-deep) 100%);
  }
  .holder-name {
    position: absolute; left: 41px; top: 40px;
    font-size: 40px; color: var(--text-white); letter-spacing: .5px;
  }
  .holder-name .first { font-weight: 600; }
  .holder-name .last { font-weight: 300; }
  .name-rule {
    position: absolute; left: 41px; top: 98px; width: 248px; height: 4px;
    background: var(--text-white); border-radius: 2px;
  }
  .brand-name {
    position: absolute; color: var(--silver); font-weight: 800;
    line-height: 1; letter-spacing: 4px;
  }
  .card--front .brand-name { left: 372px; top: 52px; font-size: 128px; }
  .address {
    position: absolute; left: 41px; top: 218px; width: 220px;
    font-size: 17px; line-height: 26px; color: var(--text-soft); font-weight: 300;
  }
  .contact-list {
    position: absolute; left: 41px; top: 318px; list-style: none;
    font-size: 15px; line-height: 21px; color: var(--text-soft); font-weight: 300;
  }
  .contact-list li { display: flex; align-items: center; gap: 9px; }
  .contact-list svg { width: 12px; height: 12px; fill: var(--text-soft); flex: none; }

  /* back */
  .back-photo {
    position: absolute; left: 0; top: 0; width: 100%; height: 212px;
    background: radial-gradient(ellipse at 50% 30%, #4a4a4e 0%, var(--mesh-mid) 35%, var(--mesh-dark) 75%, var(--card-black) 100%);
  }
  .card--back .brand-name { left: 186px; top: 52px; font-size: 128px; }
  .legal-suffix {
    position: absolute; left: 590px; top: 140px;
    font-size: 26px; font-weight: 600; color: var(--muted-grey);
  }
  .service-band {
    position: absolute; left: 0; top: 212px; width: 100%; height: 66px;
    background: var(--card-black);
  }
  .service-title {
    position: absolute; left: 48px; top: 216px;
    font-size: 50px; font-weight: 800; font-style: italic;
    color: var(--text-white); letter-spacing: 1px;
  }
  .service-panel {
    position: absolute; left: 0; top: 284px; width: 100%; height: 130px;
    background: var(--service-band);
  }
  .service-list {
    position: absolute; top: 298px; list-style: none;
    font-size: 15px; line-height: 26px; color: var(--service-text);
  }
  .service-list--left { left: 100px; }
  .service-list--right { left: 473px; }
  .service-list li { display: flex; align-items: center; gap: 12px; }
  .service-list li::before {
    content: ""; width: 16px; height: 16px; background: var(--bullet-dark);
    border-radius: 2px; flex: none;
  }
</style>
</head>
<body>
<main class="canvas">
  <section class="card card--front">
    <div class="front-photo" role="img" aria-label="Photo of a road train with side-tipper trailers on red outback dirt, under a dark metal mesh texture"></div>
    <h1 class="holder-name"><span class="first">Dean</span> <span class="last">Harlow</span></h1>
    <div class="name-rule"></div>
    <div class="brand-name">KRX</div>
    <p class="address">your address,home no road no 123,gpo code country</p>
    <ul class="contact-list">
      <li><svg viewBox="0 0 24 24"><path d="M6.6 10.8a15 15 0 0 0 6.6 6.6l2.2-2.2a1 1 0 0 1 1-.25 11.4 11.4 0 0 0 3.6.57 1 1 0 0 1 1 1V20a1 1 0 0 1-1 1A17 17 0 0 1 3 4a1 1 0 0 1 1-1h3.5a1 1 0 0 1 1 1c0 1.25.2 2.45.57 3.6a1 1 0 0 1-.25 1z"/></svg>+ 61 400 000 000</li>
      <li><svg viewBox="0 0 24 24"><path d="M3 9c0-3 4-5 9-5s9 2 9 5v2h-5V8H8v3H3zM6 12h12l2 8H4z"/></svg>+ 61 2 9000 0000</li>
      <li><svg viewBox="0 0 24 24"><path d="M2 5h20v14H2zm2 2v.5l8 5 8-5V7z"/></svg>dean@krxhaulage.com.au</li>
      <li><svg viewBox="0 0 24 24"><circle cx="12" cy="12" r="9" fill="none" stroke="#e4e4e6" stroke-width="2.5"/><path d="M3 12h18M12 3c3 3 3 15 0 18M12 3c-3 3-3 15 0 18" fill="none" stroke="#e4e4e6" stroke-width="2"/></svg>www.krxhaulage.com.au</li>
    </ul>
  </section>

  <section class="card card--back">
    <div class="back-photo" role="img" aria-label="Dark metal hexagon mesh texture"></div>
    <div class="brand-name">KRX</div>
    <div class="legal-suffix">Pty Ltd</div>
    <div class="service-band"></div>
    <h2 class="service-title">OUR SERVICE</h2>
    <div class="service-panel"></div>
    <ul class="service-list service-list--left">
      <li>What is Lorem Ipsum?</li>
      <li>What is Lorem Ipsum?</li>
      <li>What is Lorem Ipsum?</li>
      <li>What is Lorem Ipsum?</li>
    </ul>
    <ul class="service-list service-list--right">
      <li>What is Lorem Ipsum?</li>
      <li>What is Lorem Ipsum?</li>
      <li>What is Lorem Ipsum?</li>
      <li>What is Lorem Ipsum?</li>
    </ul>
  </section>
</main>
</body>
</html>
```